bargainmentor.net - Podcast Guest Marketing E-Flyer PDF

Dear Designers:I am in need of an attractive and attention-getting layout and design for a three-page marketing flyer (commonly known as a media one sheet) that will be sent via e-mail, as PDF file, to various Podcast hosts to market me as a guest on their podcasts. I want the design of the document to "mirror" the design and branding on my parent bargainmentor.net website. I am providing ALL the edited and proofread copy and content - the designer just needs to create the design for this marketing document. I want an active PDF document and icons should be used for LinkedIn, Phone, E-mail , and website- with hyperlinks that connect accordingly. I need a fast turnaround.
Updates

Dear Designers - instead of using the photo in the project file of me speaking to the audience for the banner image - I thought it would be a better idea to make this marketing piece specific to Podcast Hosts. Therefore, an image such as the one in the link below would be good to use for a banner image. https://www.pixtrove-example.net/gallery?topic=recording+booth+images&ref=qz7&view=grid&id=Kx93LmPwa2RtVbN8YcQdE4&w=1377&h=804#pic=vRmalqobet:

Target Market(s)

This PDF document will be sent to 650 Podcast hosts in North America via a broadcast e-mail.

Font styles to use
Sans Serif

Colors
ec1f27
ffffff
000000
333333
9d9d9d

Requirements
Must have
• A three-page layout that is easy to navigate in PDF form.
• Proper font styles and sizes for key emphasis areas on the document/
• Consistent branding to mirror my bargainmentor.net parent website
• Must be easy for people to read
• Attention-getting design elements and layout
• Professional and sophisticated design
• Icons for contact information
Should not have
• Should not be cluttered and junky-looking.
• Should not use small font sizes that makes it difficult to read.
• If Podcast hosts are interested in having me as a guest - they will read the content as required on three-pages

```html
<!DOCTYPE html>
<html lang="en">
<head>
<meta charset="utf-8">
<title>Bargain Mentor – Podcast Guest One Sheet</title>
<link href="https://fonts.googleapis.com/css2?family=Montserrat:wght@600;700;800&family=Open+Sans:ital,wght@0,400;0,600;0,700;1,400&display=swap" rel="stylesheet">
<style>
:root{
  --red:#ec1f27;
  --white:#ffffff;
  --black:#000000;
  --ink:#333333;
  --grey:#9d9d9d;
  --backdrop:#a4a4a4;
  --paper:#f1f1f1;
}
*{box-sizing:border-box;margin:0;padding:0}
html,body{width:1200px;height:724px;overflow:hidden}
body{background:var(--backdrop);font-family:"Open Sans",Arial,sans-serif;color:var(--ink);position:relative}
a{color:inherit;text-decoration:none}
.page{position:absolute;top:105px;width:350px;height:496px;background:var(--paper);box-shadow:0 2px 6px rgba(0,0,0,.25);overflow:hidden}
.page--intro{left:40px}
.page--reasons{left:432px}
.page--benefits{left:815px}
p{font-size:5.6px;line-height:1.5;text-align:center}
.heading{font-family:"Open Sans",Arial,sans-serif;font-weight:700;color:var(--red);text-align:center}
.footer{position:absolute;left:0;right:0;bottom:0;height:22px;background:var(--black);display:flex;align-items:center;justify-content:space-between;padding:0 14px;color:var(--white);font-size:6px}
.footer .contact{display:flex;align-items:center;gap:5px}
.icon{width:9px;height:9px;border-radius:50%;background:var(--red);display:flex;align-items:center;justify-content:center}
.icon svg{width:6px;height:6px}
.icon--plain{background:#555}
.brand{display:flex;align-items:center;justify-content:center;gap:5px;font-family:"Open Sans",Arial,sans-serif;font-weight:600;font-size:20px;letter-spacing:-.5px}
.brand .mark{width:20px;height:20px;background:var(--red)}
.divider{display:flex;justify-content:center;gap:2px;margin:4px auto}
.divider span{height:3px;width:22px;background:var(--red)}
.divider span+span{width:14px;background:var(--black)}

/* page 1 */
.banner{position:absolute;left:0;top:0;width:350px;height:196px;background:linear-gradient(160deg,#6b1f1c 0%,#a8948a 35%,#3a2a26 70%,#1f1818 100%)}
.banner-title{position:absolute;left:52px;top:152px;width:246px;height:42px;background:rgba(60,20,20,.75);border:1px solid var(--white);color:var(--white);text-align:center;font-family:"Montserrat",Arial,sans-serif}
.banner-title strong{display:block;font-size:13.5px;font-weight:800;margin-top:6px;letter-spacing:.3px}
.banner-title span{display:block;font-size:9px;font-weight:600;letter-spacing:.4px}
.intro-body{position:absolute;top:214px;left:26px;right:26px}
.intro-body .brand{color:var(--ink)}
.intro-body .lead{font-size:7.2px;margin-top:14px;line-height:1.3}
.intro-body .question{font-size:6.3px;font-weight:600;color:var(--black);margin-top:6px}
.intro-body .subhead{font-size:7.2px;margin:12px 0 6px}

/* page 2 */
.reasons-hero{position:absolute;left:0;top:0;width:350px;height:160px;background:linear-gradient(180deg,#d61c23 0%,var(--red) 55%,#c91a21 100%)}
.reasons-hero .brand{color:var(--white);position:absolute;top:100px;left:0;right:0}
.reasons-hero .brand .mark{background:var(--white)}
.reasons-title{position:absolute;top:131px;left:0;right:0;text-align:center;color:var(--white);font-family:"Montserrat",Arial,sans-serif;font-weight:800;font-size:7.4px;line-height:1.25}
.reason-list{position:absolute;top:167px;left:22px;right:22px;list-style:none;counter-reset:r}
.reason-list li{counter-increment:r;margin-bottom:8px}
.reason-list li::before{content:counter(r);display:block;width:11px;height:11px;margin:0 auto 3px;border-radius:50%;background:var(--red);color:var(--white);font-size:6.5px;font-weight:700;text-align:center;line-height:11px}

/* page 3 */
.benefits-flow{position:absolute;top:18px;left:16px;right:16px;bottom:58px;display:flex;flex-direction:column}
.benefits-intro{padding:0 8px}
.benefits-intro .heading{font-size:7px;margin-bottom:6px}
.benefits-intro p{font-size:5.3px;margin-bottom:4px}
.profit-row{display:flex;gap:8px;margin-top:12px;align-items:flex-start}
.profit{flex:1}
.profit .heading{text-align:left;font-size:7.4px;line-height:1.25}
.profit .intro{font-size:5.6px;font-weight:700;text-align:left;color:var(--black);margin:5px 0 4px;line-height:1.3}
.profit ul{list-style:none}
.profit li{display:flex;gap:3px;font-size:4.8px;line-height:1.4;margin-bottom:4px}
.profit li svg{flex:0 0 5px;width:5px;height:5px;margin-top:1px}
.portrait{flex:0 0 90px;height:108px;margin-top:4px;background:linear-gradient(180deg,#e5e5e5 0%,#7a7a7a 60%,#2b2b2b 100%)}
.quote{font-size:4.8px;line-height:1.45;font-style:italic;text-align:left}
.quote--one{margin-top:12px}
.quote--two{margin-top:10px}
.attribution{align-self:flex-end;font-size:5.3px;line-height:1.45;text-align:center;margin-top:5px;padding-right:10px}
.attribution b{color:var(--red)}
.note{margin-top:auto;color:var(--red);font-size:5.6px;font-weight:700}
.media-band{position:absolute;left:0;right:0;bottom:0;height:52px;background:var(--red);color:var(--white);text-align:center}
.media-band p{font-size:5.8px;font-weight:600;margin-top:5px;line-height:1.35}
.badges{display:flex;justify-content:center;gap:4px;margin-top:5px}
.badges span{width:57px;height:16px;background:var(--white)}
</style>
</head>
<body>

<section class="page page--intro">
  <div class="banner" role="img" aria-label="Banner photo of a speaker presenting to a seated audience in a conference room"></div>
  <div class="banner-title"><strong>TURKEY SOLUTIONS</strong><span>TO IMPROVE NEGOTIATING SKILLS</span></div>
  <div class="intro-body">
    <div class="brand"><span class="mark"></span>Bargain Mentor</div>
    <h1 class="heading lead">MEET BARGAIN MENTOR® DANIEL R. KESTREL – THE EXPERT YOU NEED AS A GUEST ON YOUR PODCAST</h1>
    <div class="divider"><span></span><span></span></div>
    <p class="question">Are you looking for a relevant and appealing topic and an engaging subject matter expert who can provide measurable value &amp; life-changing tips to the listeners of your podcast?</p>
    <h2 class="heading subhead">Why Negotiating and Decision Making Should Be Topics on Your Podcast</h2>
    <p>Regardless of your podcast theme – it's important to remember that your listeners are negotiating all the time – in their personal lives, social lives, and especially in their business lives. Negotiating is an essential life skill. Everyone can improve his or her negotiating skills, and Daniel is the expert who can provide the answers your people crave. Your podcast listeners will benefit from Daniel's proven, practical, and relevant negotiating strategies and tips that will improve results and outcomes in all types of personal and business negotiations.</p>
    <h2 class="heading subhead">Reasons to Book Daniel R. Kestrel As a Guest on Your Podcast</h2>
    <p>Daniel is a dynamic, thought-provoking, engaging, captivating, and entertaining speaker who will share some great personal stories to help your listeners better understand and relate to the topic of negotiating and decision-making dynamics. He will indeed challenge the "status quo."</p>
  </div>
  <footer class="footer">
    <a class="contact" href="tel:5550142290"><span class="icon"><svg viewBox="0 0 10 10"><path d="M2 1l2 2-1 1.3c.6 1.2 1.5 2.1 2.7 2.7L7 6l2 2-1.3 1.3C4.5 9 1 5.5.7 2.3z" fill="#fff"/></svg></span>555-014-2290</a>
    <a class="contact" href="https://bargainmentor.net"><span class="icon"><svg viewBox="0 0 10 10"><circle cx="5" cy="5" r="4" fill="none" stroke="#fff"/><path d="M1 5h8M5 1c-2 2.5-2 5.5 0 8M5 1c2 2.5 2 5.5 0 8" fill="none" stroke="#fff" stroke-width=".7"/></svg></span>www.bargainmentor.net</a>
    <a class="contact" href="mailto:daniel@kestrelmail.net"><span class="icon"><svg viewBox="0 0 10 10"><rect x="1" y="2.5" width="8" height="5" fill="none" stroke="#fff"/><path d="M1 2.5l4 3 4-3" fill="none" stroke="#fff"/></svg></span>daniel@kestrelmail.net</a>
  </footer>
</section>

<section class="page page--reasons">
  <div class="reasons-hero">
    <div class="brand"><span class="mark"></span>Bargain Mentor</div>
    <h2 class="reasons-title">SIX REASONS TO<br>BOOK DANIEL R. KESTREL AS A GUEST ON YOUR PODCAST</h2>
  </div>
  <ol class="reason-list">
    <li><p>Daniel is a dynamic, thought-provoking, engaging, captivating, and entertaining speaker who will share some great personal stories to help your listeners better understand and relate to the topic of negotiating and decision-making dynamics. He will indeed challenge the "status quo."</p></li>
    <li><p>Daniel is the founder of bargainmentor.net® and is an internationally recognized expert and highly rated speaker on the topics of negotiating and decision-making dynamics that affect negotiated outcomes. His versatility and commitment to proper preparation will ensure that his content is tailored to address the theme of your podcast and the needs of your listeners.</p></li>
    <li><p>His five-star-rated presentations and training programs have been delivered around the world to small and medium-sized businesses, Fortune 500 corporations, and large industry, trade, and peer-to-peer associations such as Rising Leaders Circle and Founders Network Guild.</p></li>
    <li><p>Daniel has personally trained over 50,000 people of all experience levels, across multiple industries, in 31 countries how to negotiate more effectively.</p></li>
    <li><p>With formal training in broadcasting and media arts, Daniel provides 30 years of experience as a professional speaker who can provide your listeners with valuable insights, solutions, and answers to address listeners' challenges and questions.</p></li>
    <li><p>Daniel is the creator of the best-selling Deal Builder Toolkit Audio Learning Program – designed to be an effective all-in-one learning solution that helps people improve their negotiating capabilities and skills. He is also the host of his soon-to-be-launched Podcast – Learn How to Negotiate.</p></li>
  </ol>
  <footer class="footer">
    <a class="contact" href="https://profiles.example/danielkestrel"><span class="icon icon--plain"></span>profiles.example/danielkestrel</a>
    <a class="contact" href="https://bargainmentor.net"><span class="icon icon--plain"><svg viewBox="0 0 10 10"><circle cx="5" cy="5" r="4" fill="none" stroke="#fff"/><path d="M1 5h8M5 1c-2 2.5-2 5.5 0 8M5 1c2 2.5 2 5.5 0 8" fill="none" stroke="#fff" stroke-width=".7"/></svg></span>www.bargainmentor.net</a>
  </footer>
</section>

<section class="page page--benefits">
  <div class="benefits-flow">
    <div class="benefits-intro">
      <h2 class="heading">How Podcast Listeners Will Benefit</h2>
      <p>Most people are intimidated by the prospect and process of negotiating – and often view negotiating as an uncomfortable haggling and bargaining process that may involve confrontation, anxiety, and stress. If podcast listeners are like most people – then they probably are concerned about being taken advantage of – or that they are missing out on potential opportunities in their personal, social, and business negotiations.</p>
      <p>To alleviate your listeners' concerns, Daniel will provide them with easy-to-understand negotiating strategies, tactics, phrases, and tips they can immediately apply – the moment the podcast episode ends. Your listeners will feel more confident when they are equipped with the powerful and beneficial strategies and techniques that will help them save/make money and arrive at better outcomes when negotiating with customers, clients, suppliers, contractors, financial institutions, retailers, co-workers, colleagues, and family members.</p>
    </div>
    <div class="profit-row">
      <div class="profit">
        <h2 class="heading">Three Ways You Can Profit From Booking Daniel R. Kestrel on Your Podcast</h2>
        <p class="intro">Upon mutual agreement, podcast hosts and listeners can have access to the following money-saving and profit-generating opportunities:</p>
        <ul>
          <li><svg viewBox="0 0 10 10"><path d="M1 5l3 3 5-7" fill="none" stroke="#ec1f27" stroke-width="2"/></svg><span>Podcast hosts will be provided with a specific promotional code to share with your listeners that will entitle them to receive a special one-time discount of $19.95US off the purchase of the MP3 download of the Deal Builder Toolkit Audio Learning Program available on my online store. Complete download and purchase instructions will be provided to podcast hosts to publish in your notes and also communicate to your listeners.</span></li>
          <li><svg viewBox="0 0 10 10"><path d="M1 5l3 3 5-7" fill="none" stroke="#ec1f27" stroke-width="2"/></svg><span>Podcast hosts will receive a 10% commission payable on the net sales dollar revenue generated from the sale of MP3 downloads of Daniel's Deal Builder Toolkit Audio Learning Program.</span></li>
          <li><svg viewBox="0 0 10 10"><path d="M1 5l3 3 5-7" fill="none" stroke="#ec1f27" stroke-width="2"/></svg><span>Podcast hosts will receive a 10% referral fee for any corporation or association that books Daniel for a presentation, seminar, or learning workshop that directly results from my participation on your podcast.</span></li>
        </ul>
      </div>
      <div class="portrait" role="img" aria-label="Black and white portrait of the speaker in a suit"></div>
    </div>
    <p class="quote quote--one">"Daniel Kestrel did a terrific job on my podcast. His negotiating insights and tips were well received by my listeners, and he was an engaging, knowledgeable, and entertaining guest. Given my expertise in real estate, I thought I was a good negotiator – until Daniel taught me a few new strategies and tips during the podcast. I would recommend Daniel to any podcast host – he is a pro and his topics are relevant and can benefit everyone."</p>
    <p class="attribution">Carl Benton <b>(Podcast Host)</b><br>Property Growth Summit Podcast, Riverton, Texas</p>
    <p class="quote quote--two">"A very engaging, entertaining, and inspirational speaker who provided very useful information, strategies, and tips to apply to all my future negotiations." "Thank you to Founders Guild North for booking this speaker! I learned some things that I can address immediately and a lot of material that I need to practice. Great session!"<br>Daniel was an outstanding speaker on the topic of negotiating! He was one of my favorite speakers ever! Daniel was a real 'teacher' versus other typical speakers who spend two hours bragging or promoting their book." "Daniel was a very knowledgeable and well-prepared speaker who provided helpful tips and scripts throughout the entire presentation! I would love to learn more from this speaker."</p>
    <p class="attribution">RT Halloway <b>(CEO &amp; President)</b></p>
    <p class="note">Note: Discount and commission payments are subject to agreement to standard terms &amp; conditions.</p>
  </div>
  <div class="media-band">
    <p>Daniel has appeared on radio programs, written articles or contributed to<br>articles for the following media outlets:</p>
    <div class="badges"><span></span><span></span><span></span><span></span><span></span></div>
  </div>
</section>

</body>
</html>
```